50th Invite

Design a 50th birthday invite.

Key essentials to communicate are:

Date: 14 December 2019
Time: 7pm for 7.30pm departure
Birthday person: Glen
Theme: Boat Party
Location: Berth K4 27, Fernquay

Other than that will leave to your creativity. Just for clarity, the above is info to be communicated somehow on the invite, I dont want it to be simply copied.

i would like a luxury boat theme, think Miami, Bahamas etc etc, photos or drawings OK

```html
<!DOCTYPE html>
<html lang="en">
<head>
<meta charset="utf-8">
<title>Glen's 50th Birthday Invite</title>
<link rel="stylesheet" href="https://fonts.googleapis.com/css2?family=Questrial&family=Libre+Baskerville:wght@400;700&display=swap">
<style>
  :root {
    --page: #f1f2f4;
    --sea-deep: #2c6890;
    --sea-mid: #3f86ad;
    --sea-shallow: #74aec6;
    --sand: #ebbcaa;
    --sand-light: #f2cbbb;
    --line: #ffffff;
    --gold-dark: #a77b12;
    --gold: #e2b93a;
    --gold-light: #fbe9a0;
    --sans: "Questrial", "Century Gothic", sans-serif;
    --serif: "Libre Baskerville", "Times New Roman", serif;
  }
  * { margin: 0; padding: 0; box-sizing: border-box; }
  html, body {
    width: 1200px;
    height: 1200px;
    overflow: hidden;
    background: var(--page);
  }
  .invite {
    position: absolute;
    left: 200px;
    top: 30px;
    width: 800px;
    height: 1140px;
    overflow: hidden;
    box-shadow: 0 6px 24px rgba(0, 0, 0, 0.18);
  }
  .invite__photo {
    position: absolute;
    inset: 0;
    background:
      radial-gradient(ellipse 330px 560px at 790px 240px, var(--sand-light) 0%, var(--sand) 62%, rgba(160, 200, 210, 0.6) 80%, rgba(116, 174, 198, 0) 100%),
      radial-gradient(ellipse 420px 700px at 700px 500px, var(--sea-shallow) 0%, rgba(116, 174, 198, 0) 100%),
      linear-gradient(100deg, var(--sea-deep) 0%, var(--sea-mid) 55%, var(--sea-shallow) 100%);
  }
  .invite__art {
    position: absolute;
    inset: 0;
    width: 800px;
    height: 1140px;
  }
  .invite__name {
    position: absolute;
    left: 0;
    width: 860px;
    top: 140px;
    text-align: center;
    font-family: var(--sans);
    font-weight: 400;
    font-size: 54px;
    line-height: 60px;
    letter-spacing: 3px;
    color: var(--line);
  }
  .details {
    position: absolute;
    top: 835px;
    left: 0;
    width: 800px;
    font-family: var(--sans);
    font-variant: small-caps;
    font-size: 23px;
    letter-spacing: 1.5px;
    line-height: 32px;
    color: var(--line);
  }
  .details__row { position: relative; height: 32px; }
  .details__label {
    position: absolute;
    right: 548px;
    text-align: right;
  }
  .details__value {
    position: absolute;
    left: 300px;
    white-space: nowrap;
  }
</style>
</head>
<body>
  <main class="invite">
    <div class="invite__photo" role="img" aria-label="Aerial photo of boats on turquoise water beside a pink sand beach"></div>

    <svg class="invite__art" viewBox="0 0 800 1140" xmlns="http://www.w3.org/2000/svg">
      <defs>
        <linearGradient id="gold-fill" x1="0" y1="0" x2="0.4" y2="1">
          <stop offset="0" stop-color="#a77b12"/>
          <stop offset="0.35" stop-color="#e2b93a"/>
          <stop offset="0.6" stop-color="#fbe9a0"/>
          <stop offset="1" stop-color="#e2b93a"/>
        </linearGradient>
        <linearGradient id="gold-bar" x1="0" y1="0" x2="1" y2="0">
          <stop offset="0" stop-color="#a77b12"/>
          <stop offset="0.5" stop-color="#fbe9a0"/>
          <stop offset="1" stop-color="#a77b12"/>
        </linearGradient>
        <path id="banner-curve" d="M272 524 C 362 520, 468 548, 556 598"/>
      </defs>

      <path class="frame" fill="none" stroke="var(--line)" stroke-width="3"
            d="M64 24 H736 A40 40 0 0 0 776 64 V1074 A40 40 0 0 0 736 1114 H64 A40 40 0 0 0 24 1074 V64 A40 40 0 0 0 64 24 Z"/>

      <rect class="gold-band" x="14" y="1094" width="772" height="10" fill="url(#gold-bar)"/>

      <rect class="flag flag--left" x="32" y="46" width="128" height="104" rx="8" fill="var(--line)" opacity="0.85" role="img" aria-label="Nautical pennant flag with star"/>
      <rect class="flag flag--right" x="640" y="46" width="128" height="104" rx="8" fill="var(--line)" opacity="0.85" role="img" aria-label="Nautical pennant flag with star"/>

      <text class="age age--shadow" x="409" y="474" text-anchor="middle" font-family="Libre Baskerville, serif" font-weight="700" font-size="280" letter-spacing="-18" fill="#5a3f08" opacity="0.55">50</text>
      <text class="age" x="404" y="470" text-anchor="middle" font-family="Libre Baskerville, serif" font-weight="700" font-size="280" letter-spacing="-18" fill="url(#gold-fill)">50</text>
      <text class="age__suffix" x="582" y="306" font-family="Libre Baskerville, serif" font-size="62" fill="#fbe9a0">th</text>

      <g class="banner" fill="none" stroke="var(--line)" stroke-width="2.5">
        <path d="M258 484 C 360 478, 490 515, 572 568 L 560 612 C 480 560, 360 530, 262 534 Z"/>
      </g>
      <text class="banner__text" font-family="Questrial, sans-serif" font-size="28" letter-spacing="9" fill="var(--line)">
        <textPath href="#banner-curve">BIRTHDAY</textPath>
      </text>

      <rect class="anchors" x="360" y="713" width="82" height="80" rx="10" fill="var(--line)" opacity="0.85" role="img" aria-label="Crossed anchors emblem"/>

      <line class="details__divider" x1="274" y1="830" x2="274" y2="942" stroke="var(--gold)" stroke-width="2"/>
      <circle cx="274" cy="938" r="4" fill="none" stroke="var(--gold)" stroke-width="2"/>

      <circle class="life-ring" cx="398" cy="1003" r="40" fill="var(--line)" opacity="0.7" role="img" aria-label="Life ring emblem"/>
    </svg>

    <h1 class="invite__name">GLEN’S</h1>

    <section class="details">
      <div class="details__row"><span class="details__label">Date</span><span class="details__value">14 December 2019</span></div>
      <div class="details__row"><span class="details__label">Time</span><span class="details__value">7pm for 7.30pm departure</span></div>
      <div class="details__row"><span class="details__label">Location</span><span class="details__value">Berth K4 27, Fernquay</span></div>
    </section>
  </main>
</body>
</html>
```